Modern card design needed for building development company

We are looking for a sharp modern new look for our business cards.
We are a New Zealand based company called TKR Ventures NZ LTD that specialises in subdividing large sections, housing and commercial buildings.
We have attached a photo of the current logo and would like to see it improved somehow as it looks a bit dated.
We are open to any colours.

Target Market(s)

Investors, Property buyers

Industry/Entity Type

Investment

Contact Information for Business Card

TKR VENTURES NZ LTD
www.tkrventuresnz.example.nz

Dorian Fletcher
Phone +64 21 843 209
Email dpfletcher@mailvane.example.nz

Font styles to use
Serif
Sans Serif

Colors
0792cd
33a6d7
85cae6
6b449b
886aae
f04a50
ec1f27
f37122
f68d4d

Requirements
Must have
• Please try and make the logo more modern or if you have a similar one we would like to see it.

```html
<!DOCTYPE html>
<html lang="en">
<head>
<meta charset="utf-8">
<title>TKR Ventures NZ LTD – Business Card</title>
<link href="https://fonts.googleapis.com/css2?family=Open+Sans:wght@400;700&display=swap" rel="stylesheet">
<style>
  :root {
    --backdrop: #ebe8e3;
    --kraft-light: #c7a77c;
    --kraft: #b99868;
    --kraft-dark: #ad8c5e;
    --ink: #141210;
    --card-shadow: rgba(60, 45, 25, 0.22);
  }
  * { margin: 0; padding: 0; box-sizing: border-box; }
  html, body {
    width: 1200px;
    height: 900px;
    overflow: hidden;
    background: var(--backdrop);
    font-family: "Open Sans", Arial, sans-serif;
    color: var(--ink);
  }
  .canvas {
    position: relative;
    width: 1200px;
    height: 900px;
  }
  .card {
    position: absolute;
    width: 556px;
    height: 342px;
    background: radial-gradient(ellipse at 45% 40%, var(--kraft-light) 0%, var(--kraft) 55%, var(--kraft-dark) 100%);
    box-shadow: 0 6px 18px var(--card-shadow);
    text-align: center;
  }
  .card--contact { left: 214px; top: 85px; }
  .card--brand { left: 470px; top: 477px; }

  .contact-name {
    position: absolute;
    top: 114px;
    left: 0;
    right: 0;
    font-size: 20px;
    font-weight: 700;
    letter-spacing: 0.3px;
  }
  .contact-lines {
    position: absolute;
    top: 164px;
    left: 0;
    right: 0;
    list-style: none;
    font-size: 13.5px;
    line-height: 21px;
    letter-spacing: 0.2px;
  }

  .brand-mark {
    position: absolute;
    top: 74px;
    left: 50%;
    width: 64px;
    height: 64px;
    margin-left: -32px;
    background: var(--ink);
  }
  .brand-name {
    position: absolute;
    top: 172px;
    left: 0;
    right: 0;
    font-weight: 400;
    line-height: 1;
  }
  .brand-name span { display: block; }
  .brand-name__primary { font-size: 44px; letter-spacing: 2px; }
  .brand-name__secondary { font-size: 34px; letter-spacing: 1.5px; margin-top: 4px; }
  .brand-name__suffix { font-size: 16px; letter-spacing: 1px; margin-top: 6px; }
</style>
</head>
<body>
<main class="canvas">
  <section class="card card--contact">
    <h1 class="contact-name">DORIAN FLETCHER</h1>
    <ul class="contact-lines">
      <li class="contact-phone">+64 21 843 209</li>
      <li class="contact-email">DPFLETCHER@MAILVANE.EXAMPLE.NZ</li>
      <li class="contact-web">WWW.TKRVENTURESNZ.EXAMPLE.NZ</li>
    </ul>
  </section>

  <section class="card card--brand">
    <div class="brand-mark" aria-hidden="true"></div>
    <p class="brand-name">
      <span class="brand-name__primary">TKR</span>
      <span class="brand-name__secondary">VENTURES</span>
      <span class="brand-name__suffix">NZ LTD</span>
    </p>
  </section>
</main>
</body>
</html>
```